Swimming Pool Service Website needed!!!

Hi Everyone! Thanks for looking at my contest. I PROMISE to provide excellent feedback during this process.

I am starting a new swimming pool business cleaning company in San Diego, California and would like your help in making it similar to one of these two websites that are already functioning.

http://www.brightmeadowhub.example/services-repair.html

http://tryvelmarktide.example/commercial-pool-cleaning.php

I like these two because they are easy to read, classy, sophisticated and have nice pictures of really clean & clear pools.

I really like the blue on white color format.

I do not have a logo, but the name of my company is HARBORLINE POOL SERVICE.

My tag line is: Water so bright, you'll want to dive right in. (does not need to have the quotes around "in"...maybe just italics for this word IN?) You decide for me.

I would like to have a logo designed that incorporates some sort of easy to read letters. I do not want cursive (handwriting) letters. I thought about having a "reflection" of letters (mirror image), but think that this will be hard to read from far away. Maybe you can surprise me and come up with an idea that works using the a mirror image....but I'm not sure. I was leaning toward plain old BLOCK letters as I think it would be easy to read on my truck.

I would like to have 5 pages on my website:
1) Home
2) About Us (Know Your Poolman) / Why Hire Us
3) Services Offered
4) FAQ's
5) Contact

I am looking for a fully-functioning website (coded). Upon selection of the design winner, I am offering to increase the budget/payment by $100-$125 for the coding of all the pages. So anyone looking at participating in this contest, should be willing and able to provide the coding to the webpages that i've requested.

Target Market(s)

Upper middle-class homeowners who have a pool

Industry/Entity Type

Pool Service

Number of Pages Required

5+ page

Font styles to use
Serif

Colors
0455a3
3276b5
85acd3
85cae6
ffffff
33a6d7
0592cd

Requirements
Must have
• The Home page must have this picture highlighted in the top of the page:
• http://www.dunecrestwaterman.example/
• Must have pictures of some high-end pools. Any that you can find on the internet are wonderful.
• Must have a table on the right of the home page that mentions the service areas that we go to:
• • Carmel Valley (92130)
• • Del Mar (92014)
• • Rancho Santa Fe (92067)
• • Solana Beach (92075)
• • Santaluz (92127)
• • Cardiff (92007)
• • Encinitas (92024)
• • Carlsbad (92009, 92008)
• • La Jolla (92037)
• • Pacific Beach (92109)
• • Mira Mesa (92126)
• • Sorrento Valley (92121)
• • Clairemont (92117)
• • Rancho Bernardo (92127, 92128)
• • Rancho Penasquitos (92129)
• • Poway (92064)
Nice to have
• Maybe incorporate some pictures of some kids (or families) playing in pools on the Why Hire Us page?
• I also like the feel of this website, but posting this page just for reference so you can get a feel more of what I like:
• http://www.ferrovaletide.example/
• I like the FAQ's page from this website. I like how you can click on the question and then it pops up with the answer. http://www.quillbrookaquacare.example/pool-spa-fountain-faqs/

```html
<!DOCTYPE html>
<html lang="en">
<head>
<meta charset="utf-8">
<title>Harborline Pool Service</title>
<link href="https://fonts.googleapis.com/css2?family=Arimo:wght@400;700&family=Cinzel:wght@400;600&family=Roboto+Condensed:ital,wght@0,400;1,400&display=swap" rel="stylesheet">
<style>
:root{
  --navy:#0455a3;
  --brand:#1f4f8f;
  --mid:#3276b5;
  --sky:#33a6d7;
  --panel:#3fa3dc;
  --field:#b4dcf3;
  --ocean-1:#0a5fa8;
  --ocean-2:#1c86cc;
  --footer:#2a8fcb;
  --text:#555;
  --rule:#b9b9b9;
  --white:#fff;
}
*{box-sizing:border-box;margin:0;padding:0}
html,body{width:989px;height:1200px;overflow:hidden}
body{font-family:"Arimo",Arial,sans-serif;color:var(--text);font-size:9.6px;line-height:14.2px;position:relative}
.ocean{position:absolute;inset:0;background:linear-gradient(180deg,var(--ocean-2),var(--ocean-1) 50%,var(--ocean-2))}
.page{position:absolute;left:129px;top:0;width:728px;height:1200px;background:var(--white)}
.abs{position:absolute}
/* header */
.brand{left:14px;top:32px;display:flex;align-items:center;gap:6px;font-family:"Cinzel",serif;font-weight:400;font-size:16.5px;color:var(--brand);letter-spacing:.3px}
.brand-dot{width:10px;height:10px;border-radius:50%;background:var(--sky)}
.call{left:556px;top:17px;display:flex;gap:6px;align-items:center}
.call-label{font-family:"Roboto Condensed",sans-serif;color:var(--mid);font-size:12px;line-height:13px}
.call-num{font-family:"Roboto Condensed",sans-serif;color:var(--brand);font-size:17.5px;line-height:20px}
.nav{left:255px;top:62px;display:flex;align-items:center;font-size:11.2px;color:#222}
.nav span{padding:0 10px;border-left:1px solid #bbb;line-height:12px}
.nav span:first-child{border:0;padding-left:4px;position:relative}
.nav span:first-child::after{content:"";position:absolute;left:1px;right:-4px;bottom:-7px;height:2px;background:var(--brand)}
/* hero */
.hero{left:0;top:106px;width:728px;height:290px;background:linear-gradient(180deg,#eaf2f8 0%,#bcd6ea 20%,#4a8fc5 30%,#2b78be 55%,#6fb5e3 80%,#b7dcf3 100%)}
.tagline{left:160px;top:344px;width:410px;height:38px;background:rgba(120,140,150,.55);color:var(--white);font-family:"Roboto Condensed",sans-serif;font-style:italic;font-size:17.5px;line-height:38px;text-align:center;white-space:nowrap}
.inquiry{left:491px;top:98px;width:192px;height:210px;background:var(--panel);border:2px solid #2f7fbf;padding:9px 12px;box-shadow:0 2px 4px rgba(0,0,0,.3)}
.inquiry h2{font-family:"Arimo",sans-serif;font-weight:700;color:var(--white);font-size:16.5px;line-height:20px;margin-bottom:7px}
.field{background:var(--field);height:17px;margin-bottom:6px;font-size:8.5px;line-height:17px;padding-left:7px;color:#456}
.field.area{height:57px;line-height:14px;padding-top:2px}
.submit{display:inline-block;background:var(--brand);color:var(--white);font-weight:700;font-size:10.5px;padding:3px 7px;margin-top:1px}
.dots{left:345px;top:404px;display:flex;gap:3px}
.dots i{width:6px;height:6px;border-radius:50%;background:#999}
.dots i:first-child{background:var(--brand)}
/* feature cards */
.card{top:428px;width:218px;height:90px;border:1px solid #999;border-radius:5px;padding:9px 8px 0 65px}
.card h3{font-family:"Roboto Condensed",sans-serif;font-weight:400;color:var(--brand);font-size:13.5px;line-height:16px;margin-bottom:2px}
.card p{font-size:9.2px;line-height:14px}
.card .more{position:absolute;right:12px;bottom:4px;color:#222;text-decoration:underline;font-size:9.5px;background:var(--white)}
.card svg{position:absolute;left:6px;top:10px}
/* sections */
h2.sec{font-family:"Cinzel",serif;font-weight:600;color:var(--navy);font-size:14.5px;line-height:18px;border-bottom:1px dashed var(--rule);padding-bottom:3px;margin-bottom:10px}
.link{color:#222;text-decoration:underline;font-size:10.5px}
.left{left:14px;width:449px}
.divider{left:477px;top:546px;height:496px;border-left:1px dashed var(--rule)}
.areas{display:grid;grid-template-columns:153px 148px 168px;row-gap:1px;width:470px;white-space:nowrap}
.bul{position:relative;padding-left:8px}
.bul::before{content:"";position:absolute;left:0;top:3px;border-left:4px solid var(--mid);border-top:4px solid transparent;border-bottom:4px solid transparent}
.quote{position:relative;padding-left:27px;margin-bottom:12px;color:#333;line-height:15.5px}
.quote::before{content:"\201C";position:absolute;left:0;top:-8px;font-family:Georgia,serif;font-size:36px;color:#aaa;line-height:36px}
.quote .close{font-family:Georgia,serif;font-size:36px;color:#aaa;vertical-align:-16px;margin-left:6px;line-height:0}
.right{left:497px;width:226px}
.svc li{list-style:none;margin-bottom:2.4px;padding-left:12px;font-size:9.3px;line-height:13.6px}
.svc li::before{left:0;top:3px}
/* footer */
.footer{left:-2px;top:1109px;width:732px;height:91px;background:var(--footer);color:var(--white)}
.fnav{left:15px;top:20px;display:flex;font-size:10.2px}
.fnav span{padding:0 9px;border-left:1px solid #cde}
.fnav span:first-child{border:0;padding-left:0}
.addr{left:20px;top:42px;font-size:10.5px}
.follow{left:457px;top:21px;font-size:10.5px}
.soc{left:457px;top:40px;display:flex;gap:8px}
.soc i{width:18px;height:18px;border-radius:3px;background:#5aa7d6;border:1px solid #cde}
.flogo{left:585px;top:20px;font-family:"Cinzel",serif;font-size:15px;line-height:17px;text-align:center;width:135px}
.copy{left:0;width:732px;top:76px;text-align:center;font-size:8.5px}
</style>
</head>
<body>
<div class="ocean" role="img" aria-label="Deep blue rippled ocean water background"></div>
<div class="page">
  <div class="abs brand"><span>HARBORLINE POOL SERVICE</span><span class="brand-dot"></span></div>
  <div class="abs call">
    <svg width="22" height="24" viewBox="0 0 22 24"><circle cx="11" cy="12" r="10" fill="none" stroke="#1f4f8f" stroke-width="1.5"/><path d="M8 6c-2 2-2 8 2 12l2-2-2-3 1-2 2 0 1-3z" fill="#1f4f8f"/></svg>
    <div><div class="call-label">Call Us Today</div><div class="call-num">555-014-2290</div></div>
  </div>
  <div class="abs nav"><span>Home</span><span>About Us</span><span>Services Offered</span><span>FAQ’s</span><span>Why Hire Us</span><span>Contact Us</span></div>

  <div class="abs hero" role="img" aria-label="Photo of a clear blue swimming pool with a chrome ladder and ocean horizon"></div>
  <div class="abs tagline">Water so bright, you’ll want to dive right <em>in</em>.</div>
  <div class="abs inquiry">
    <h2>Quick Inquiry</h2>
    <div class="field">Name</div>
    <div class="field">Email</div>
    <div class="field">Mobile</div>
    <div class="field area">Questions / Comments</div>
    <span class="submit">Submit</span>
  </div>
  <div class="abs dots"><i></i><i></i><i></i><i></i><i></i></div>

  <div class="abs card" style="left:14px">
    <svg width="50" height="44" viewBox="0 0 50 44"><path d="M2 20L18 6l16 14h-5v14H7V20z" fill="#1f4f8f"/><rect x="14" y="24" width="7" height="10" fill="#fff"/><path d="M28 20v18M36 20v18M28 26h8M28 32h8" stroke="#1f4f8f" stroke-width="2"/><path d="M26 40h22M30 44h18" stroke="#1f4f8f" stroke-width="2"/></svg>
    <h3>Residential Services</h3>
    <p>Harborline Pool Service offers maintenance and repairs for all residential pools.</p>
    <span class="more">Read More</span>
  </div>
  <div class="abs card" style="left:254px">
    <svg width="50" height="44" viewBox="0 0 50 44"><path d="M4 36V16h6v20M12 36V6h6v30M20 36V20h6v16" fill="none" stroke="#1f4f8f" stroke-width="2"/><path d="M30 20v16M38 20v16M30 26h8" stroke="#1f4f8f" stroke-width="2"/><path d="M2 38h46M8 42h40" stroke="#1f4f8f" stroke-width="2"/></svg>
    <h3>Commercial Services</h3>
    <p>we do it all! Health Clubs, Schools, Hotels, Motels, Apartments, Condominiums</p>
    <span class="more">Read More</span>
  </div>
  <div class="abs card" style="left:493px">
    <svg width="36" height="36" viewBox="0 0 36 36"><circle cx="18" cy="18" r="15" fill="none" stroke="#1f4f8f" stroke-width="2"/><path d="M14 9c-3 3-3 12 3 18l3-3-3-4 1-3 3 0 1-5z" fill="#1f4f8f"/></svg>
    <h3>Quick Inquiry</h3>
    <p>Please call or E-Mail us with any questions about our pool service, or to schedule a free pool...</p>
    <span class="more">Read More</span>
  </div>

  <div class="abs left" style="top:547px">
    <h2 class="sec">Welcome to Harborline Pool Service</h2>
    <p>At Harborline Pool Service, we understand that your pool is an important investment. Whether it’s part of your business or in your backyard, it needs to be well taken care of to ensure its longevity and your peace of mind. At Harborline Pool Service, we pride ourselves in setting the standard in our industry. What sets us apart from our competition is our commitment to excellence. Our exceptional service and competitive price make us the clear choice for your pool service needs.</p>
    <p style="margin-top:14px">Harborline Pool Service has been providing spectacular pool &amp; spa cleaning and maintenance service for over 7 years. Our technicians are professionally trained and are committed to providing outstanding customer service through our honest...</p>
    <p style="margin-top:5px"><span class="link">Read More</span></p>
  </div>

  <div class="abs left" style="top:764px">
    <h2 class="sec">Service Areas That We Go To:</h2>
    <div class="areas">
      <div class="bul">Carmel Valley (92130)</div><div class="bul">Mira Mesa (92126)</div><div class="bul">Sorrento Valley (92121)</div>
      <div class="bul">Del Mar (92014)</div><div class="bul">Encinitas (92024)</div><div class="bul">Clairemont (92117)</div>
      <div class="bul">Rancho Santa Fe (92067)</div><div class="bul">Carlsbad (92009, 92008)</div><div class="bul">Rancho Bernardo (92127, 92128)</div>
      <div class="bul">Solana Beach (92075)</div><div class="bul">La Jolla (92037)</div><div class="bul">Rancho Penasquitos (92129)</div>
      <div class="bul">Santaluz (92127)</div><div class="bul">Pacific Beach (92109)</div><div class="bul">Poway (92064)</div>
      <div class="bul">Cardiff (92007)</div>
    </div>
  </div>

  <div class="abs left" style="top:917px">
    <h2 class="sec">Customer Reviews</h2>
    <p class="quote">Working with Miles is terrific. His education and professional background sets him apart from all the other pool cleaners. He has excellent communication with us and he shows up when he says he will. Harborline is the only pool care company I have ever recommended to my friends<span class="close">&#8221;</span></p>
    <p class="quote">I was looking for a pool service company and I’m so glad I found Harborline! Miles, the owner, is an honest business man. Don’t go anywhere else! You’ll be surprised at what a great communicator Miles is and the service that he does is awesome!<span class="close">&#8221;</span></p>
    <p><span class="link">Read More</span></p>
  </div>

  <div class="abs divider"></div>

  <div class="abs right" style="top:547px">
    <h2 class="sec">Services Offered</h2>
    <p style="margin-bottom:8px;line-height:12.5px;width:214px">Harborline Pool Service is a full service company. We cover the complete spectrum of regular service and repair. From start-ups to restoring swampy pools, repairing or replacing equipment, Harborline does it all</p>
    <ul class="svc">
      <li class="bul">Swimming Pool and Spa Cleaning</li>
      <li class="bul">Install and repair lighting</li>
      <li class="bul">New Pool and Spa Start Ups</li>
      <li class="bul">Leak Detection &amp; Salt System Conversions</li>
      <li class="bul">Troubleshoot and Repair pumps, filters, heaters and heat exchangers</li>
      <li class="bul">Fountain Cleaning and Service</li>
      <li class="bul">Tile Cleaning &amp; Restoration</li>
      <li class="bul">Licensed and Bonded Swimming Pool Technicians</li>
      <li class="bul">CPO (Certified Pool Operator) Insured</li>
      <li class="bul">Low Rates for Repairs, Maintenance, Cleaning</li>
      <li class="bul">Reliable &amp; affordable pool &amp; spa maintenance</li>
      <li class="bul">Friendly assistance from the staff</li>
      <li class="bul">Brushing walls and tile cleaning</li>
      <li class="bul">Salt water system maintenance</li>
      <li class="bul">Pool leakage detection and repairs</li>
      <li class="bul">Noisy pool motor repairs</li>
      <li class="bul">Prompt swimming pool cleaning each week Vacuuming pool floor and steps</li>
      <li class="bul">Eliminating leaves and debris</li>
      <li class="bul">Cleaning out debris in skimmer and pool pump basket</li>
      <li class="bul">Making your pool and spa crystal clear with balanced chemicals</li>
    </ul>
  </div>
  <div class="abs" style="left:666px;top:1066px"><span class="link">Read More</span></div>

  <div class="abs footer">
    <div class="abs fnav"><span>Home</span><span>About Us</span><span>Services Offered</span><span>FAQ’s</span><span>Why Hire Us</span><span>Contact Us</span></div>
    <div class="abs addr">Street Name City Name State Zipcode &nbsp;| &nbsp;Phone: 555-014-2290</div>
    <div class="abs follow">Follow Us On</div>
    <div class="abs soc"><i></i><i></i><i></i></div>
    <div class="abs flogo">HARBORLINE<br>POOL SERVICE</div>
    <div class="abs copy">Copyright © 2015, &nbsp;HarborlinePoolService.example. | &nbsp;All Rights Reserved.</div>
  </div>
</div>
</body>
</html>
```